Infographic Illustration Design Project

We need an infographic fo a foundation based in Vancouver, BC, Canada.
We need it to be bold and colourful and show what we've done as a foundation over the last year.
Here is the content needed to put into the infographic:
BRIGHT HARBOR FOUNDATION
INFOGRAPHIC
www.brightharbor-example.org
Top section
Image: Map of the world
Text: Where Bright Harbor Foundation is Investing
(see image here for where to pins on the map of the world) http://www.brightharbor-example.org/about/about.aspx?page=2
Next section
What is the Bright Harbor Foundation Providing for Missionaries?
Image: Video camera
Text in video camera image: 82
82 Video Cameras Shipquicked Overseas
Image: Web Page
Text in web page: 116
116 Web Pages Created
Image: Dollar Bill
Text in Dollar Bill: $6,000
$6,000 in Matching Funds
Image: E-Mail
Text in E-Mail: 67
67 Fundraising Training E-Letters Sent
Missionaries Telling their Story
Image: Vidstream Video
Text: 110
110 Videos Uploaded from the Field
Image: Cell phone
Text 214
214 Text Messages Sent from the Field
Image: Poloroid photo
Text: 580
580 Photos Uploaded from the Field
Funds were raised
In MASSIVE text: $331,291.55
smaller text: Raised for Missionaries and Wired Overseas
Through various ways
Image: beer glass
Text: 1
1 Champion Who Gave Up Beer to Raise Money for Missions
Image: Wedding Cake Topper
Text: 1
1 Champion Who Gave Up their Wedding to Raise Money for Missions
Image: Birthday Present
Text: 1
1 Champion who Gave up Their Birthday to Raise Money for Missions
Image: People
Text 83
83 People Who Have Fundraised for a Missionary
*Stats are up to date as of Nov, 2012
Our website: www.brightharbor-example.org
Target Market(s)
18-60 year olds who have given to the foundation
Industry/Entity Type
Camera

```html
<!DOCTYPE html>
<html lang="en">
<head>
<meta charset="utf-8">
<title>Bright Harbor Foundation — Year in Numbers</title>
<link href="https://fonts.googleapis.com/css2?family=Arimo:wght@400;700&display=swap" rel="stylesheet">
<style>
  :root{
    --bg-top:#2f6582;
    --bg-mid:#265673;
    --bg-low:#1e4760;
    --panel:rgba(255,255,255,0.10);
    --panel-line:rgba(255,255,255,0.28);
    --white:#ffffff;
    --ink:#3a3a3a;
    --orange:#f0801f;
    --yellow:#f4d313;
    --green:#9ac53c;
    --red:#d3262d;
    --grey:#e7e7e7;
    --footer:#173a50;
  }
  *{box-sizing:border-box;margin:0;padding:0}
  html,body{width:1200px;height:3154px;overflow:hidden}
  body{
    font-family:"Arimo",Arial,sans-serif;
    color:var(--white);
    background:linear-gradient(180deg,var(--bg-top) 0%,var(--bg-mid) 45%,var(--bg-low) 100%);
    position:relative;
  }
  .masthead{position:absolute;top:26px;left:0;width:1200px;text-align:center}
  .masthead h1{font-size:42px;font-weight:700;letter-spacing:1px}
  .masthead .url{font-size:32px;font-weight:700;margin-top:10px}
  .world-map{
    position:absolute;top:140px;left:120px;width:960px;height:430px;
    border-radius:30px;
    background:radial-gradient(ellipse at 50% 45%,#e3edf3 0%,#bcd0dc 55%,rgba(188,208,220,0) 75%);
  }
  .map-caption{position:absolute;top:585px;left:0;width:1200px;text-align:center;font-size:26px;font-weight:700}
  .map-mark{position:absolute;top:500px;left:1000px;font-size:24px;font-weight:700}
  .panel{
    position:absolute;left:0;width:1200px;
    background:var(--panel);
    border-top:3px solid var(--panel-line);
    border-bottom:3px solid var(--panel-line);
  }
  .panel h2{
    font-size:32px;font-weight:700;text-align:center;
    padding:22px 0 20px;
    border-bottom:2px solid var(--panel-line);
    background:rgba(255,255,255,0.06);
  }
  .stat-row{display:flex;justify-content:center;gap:30px;margin-top:34px}
  .stat{width:230px;text-align:center}
  .tile{
    width:150px;height:150px;border-radius:22px;margin:0 auto;
    display:flex;align-items:center;justify-content:center;
    box-shadow:0 4px 0 rgba(0,0,0,0.25);
  }
  .tile svg{display:block}
  .tile.orange{background:var(--orange)}
  .tile.yellow{background:var(--yellow)}
  .tile.green{background:var(--green)}
  .tile.red{background:var(--red)}
  .tile.grey{background:var(--grey)}
  .tile.white{background:var(--white);flex-direction:column;color:var(--ink)}
  .tile .num{font-weight:700;fill:var(--ink)}
  .stat p{font-size:24px;font-weight:700;line-height:1.2;margin-top:16px}
  .video-tile .big{font-size:52px;font-weight:700;line-height:1}
  .video-tile .name{font-size:24px;font-weight:700;margin-top:10px;color:var(--ink)}
  .funds{position:absolute;top:1600px;left:0;width:1200px}
  .funds h2{text-align:center;font-size:34px;font-weight:700}
  .funds .total{display:flex;align-items:center;justify-content:center;gap:24px;margin-top:22px}
  .funds .amount{font-size:160px;font-weight:700;letter-spacing:-3px;line-height:1}
  .funds .note{text-align:center;font-size:40px;font-weight:700;margin-top:22px}
  .footnote{position:absolute;top:2428px;left:0;width:1200px;text-align:center;font-size:18px}
  .crowd{
    position:absolute;top:2470px;left:40px;width:1120px;height:590px;
    background:radial-gradient(ellipse at 50% 60%,#5c7f95 0%,#3d6680 50%,rgba(38,86,115,0) 80%);
    border-radius:40px;
  }
  .footer{
    position:absolute;top:3088px;left:0;width:1200px;height:66px;
    background:var(--footer);text-align:center;font-size:30px;font-weight:700;line-height:66px;
  }
</style>
</head>
<body>
  <header class="masthead">
    <h1>BRIGHT HARBOR FOUNDATION</h1>
    <div class="url">www.brightharbor-example.org</div>
  </header>

  <div class="world-map" role="img" aria-label="Map of the world with pins marking where Bright Harbor Foundation is investing"></div>
  <div class="map-mark">Bright Harbor</div>
  <div class="map-caption">Where Bright Harbor Foundation is Investing</div>

  <section class="panel" style="top:658px;height:430px">
    <h2>What is the Bright Harbor Foundation Providing for Missionaries?</h2>
    <div class="stat-row">
      <div class="stat">
        <div class="tile orange">
          <svg width="110" height="76" viewBox="0 0 110 76"><rect x="2" y="8" width="74" height="60" rx="8" fill="#fff"/><polygon points="80,26 106,12 106,64 80,50" fill="#fff"/><text class="num" x="39" y="50" font-size="34" text-anchor="middle">82</text></svg>
        </div>
        <p>82 Video Cameras Shipquicked Overseas</p>
      </div>
      <div class="stat">
        <div class="tile grey">
          <svg width="116" height="90" viewBox="0 0 116 90"><rect x="2" y="2" width="112" height="86" rx="4" fill="#fff" stroke="#999" stroke-width="3"/><rect x="2" y="2" width="112" height="14" fill="#bbb"/><text class="num" x="58" y="66" font-size="38" text-anchor="middle">116</text></svg>
        </div>
        <p>116 Web Pages Created</p>
      </div>
      <div class="stat">
        <div class="tile yellow">
          <svg width="124" height="72" viewBox="0 0 124 72"><rect x="2" y="2" width="120" height="68" rx="6" fill="#fff7b0" stroke="#7a6a00" stroke-width="3"/><text class="num" x="62" y="48" font-size="30" text-anchor="middle">$6000</text></svg>
        </div>
        <p>$6,000 in Matching Funds</p>
      </div>
      <div class="stat">
        <div class="tile red">
          <svg width="112" height="84" viewBox="0 0 112 84"><rect x="2" y="2" width="108" height="80" rx="4" fill="#fff"/><polyline points="2,2 56,40 110,2" fill="none" stroke="#bbb" stroke-width="3"/><text class="num" x="56" y="70" font-size="34" text-anchor="middle">67</text></svg>
        </div>
        <p>67 Fundraising Training E-Letters Sent</p>
      </div>
    </div>
  </section>

  <section class="panel" style="top:1130px;height:400px">
    <h2>Missionaries Telling their Story</h2>
    <div class="stat-row">
      <div class="stat">
        <div class="tile white video-tile"><span class="big">110</span><span class="name">Vidstream</span></div>
        <p>110 Videos Uploaded from the Field</p>
      </div>
      <div class="stat">
        <div class="tile green">
          <svg width="80" height="124" viewBox="0 0 80 124"><rect x="2" y="2" width="76" height="120" rx="12" fill="#fff"/><rect x="10" y="18" width="60" height="50" fill="#e9f3d2"/><text class="num" x="40" y="54" font-size="28" text-anchor="middle">214</text><rect x="14" y="80" width="52" height="30" rx="4" fill="#cfd8c0"/></svg>
        </div>
        <p>214 Text Messages Sent from the Field</p>
      </div>
      <div class="stat">
        <div class="tile red">
          <svg width="108" height="108" viewBox="0 0 108 108"><rect x="2" y="2" width="104" height="104" rx="4" fill="#fff"/><rect x="12" y="12" width="84" height="66" fill="#444"/><text x="54" y="56" font-size="32" font-weight="700" fill="#fff" text-anchor="middle">580</text></svg>
        </div>
        <p>580 Photos Uploaded from the Field</p>
      </div>
    </div>
  </section>

  <section class="funds">
    <h2>Funds were raised</h2>
    <div class="total">
      <svg width="190" height="150" viewBox="0 0 190 150" aria-hidden="true">
        <rect x="10" y="110" width="26" height="36" fill="#fff"/>
        <rect x="46" y="90" width="26" height="56" fill="#fff"/>
        <rect x="82" y="74" width="26" height="72" fill="#fff"/>
        <rect x="118" y="54" width="26" height="92" fill="#fff"/>
        <polyline points="6,96 60,58 96,72 160,20" fill="none" stroke="#fff" stroke-width="10"/>
        <polygon points="140,12 182,4 172,46" fill="#fff"/>
      </svg>
      <div class="amount">$331,291.55</div>
    </div>
    <div class="note">Raised for Missionaries and Wired Overseas</div>
  </section>

  <section class="panel" style="top:1944px;height:456px">
    <h2>What is the Bright Harbor Foundation Providing for Missionaries?</h2>
    <div class="stat-row">
      <div class="stat">
        <div class="tile orange">
          <svg width="100" height="116" viewBox="0 0 100 116"><rect x="6" y="16" width="64" height="96" rx="6" fill="#fbe3a0"/><ellipse cx="38" cy="16" rx="36" ry="14" fill="#fff"/><path d="M70 36 h14 a10 10 0 0 1 10 10 v28 a10 10 0 0 1 -10 10 h-14" fill="none" stroke="#fbe3a0" stroke-width="8"/><text class="num" x="38" y="76" font-size="36" text-anchor="middle">1</text></svg>
        </div>
        <p>1 Champion Who Gave Up Beer to Raise Money for Missions</p>
      </div>
      <div class="stat">
        <div class="tile green">
          <svg width="100" height="120" viewBox="0 0 100 120"><rect x="30" y="10" width="40" height="30" rx="4" fill="#fff"/><rect x="18" y="42" width="64" height="32" rx="4" fill="#fff"/><rect x="6" y="76" width="88" height="40" rx="4" fill="#fff"/><text class="num" x="50" y="68" font-size="26" text-anchor="middle">1</text></svg>
        </div>
        <p>1 Champion Who Gave Up their Wedding to Raise Money for Missions</p>
      </div>
      <div class="stat">
        <div class="tile yellow">
          <svg width="104" height="108" viewBox="0 0 104 108"><rect x="6" y="36" width="92" height="68" rx="4" fill="#fff"/><rect x="2" y="24" width="100" height="18" rx="3" fill="#fff" stroke="#ccc" stroke-width="2"/><path d="M52 24 C40 4 22 8 30 22 M52 24 C64 4 82 8 74 22" fill="none" stroke="#fff" stroke-width="6"/><text class="num" x="52" y="86" font-size="34" text-anchor="middle">1</text></svg>
        </div>
        <p>1 Champion who Gave up Their Birthday to Raise Money for Missions</p>
      </div>
      <div class="stat">
        <div class="tile red">
          <svg width="110" height="90" viewBox="0 0 110 90"><ellipse cx="55" cy="45" rx="52" ry="40" fill="#fff"/><text x="55" y="58" font-size="36" font-weight="700" fill="#d3262d" text-anchor="middle">83</text></svg>
        </div>
        <p>83 People Who Have Fundraised for a Missionary</p>
      </div>
    </div>
  </section>

  <div class="footnote">*Stats are up to date as of Nov, 2012</div>

  <div class="crowd" role="img" aria-label="Illustration of a large crowd of colourful pixel-style people standing together"></div>

  <footer class="footer">www.brightharbor-example.org</footer>
</body>
</html>
```